PPT Template Graphic Design for Firm Serving Sales & Mrkting Executives in High-Tech Comopanies

Brookvane seeks a graphic design for a PowerPoint template for corporate presentations.
We are a workforce solutions company that specializes in finding and managing contractors for sales and marketing organizations in high-tech companies. We can also manage entire processes with our 'managed services' solution, for existing clients. We are unique in our exclusive focus on sales & marketing, our consultative approach that works with clients to leverage contractors, not just to fill immediate resource gaps they may have, but also to achieve immediate and longer term business goals of their organization. We offer the dual advantage of flexibility as clients may find within a boutique firm, and the scalability of a global company which means that regardless of whether clients need one contractor or several, locally or in foreign markets, we can help.
We will use this PPT template to present what we do to help clients, and how we are different from the competition to prospective clients. We might also use this PPT template to present proposals.

Reason: We would love to see some more design options! Also, we have guaranteed the project since we first posted. Thank you!

Target Market(s)

Executives in sales and marketing organizations of high tech companies, including VP of Sales, VP marketing, CEO, CFO and heads of HR departments.

Industry/Entity Type

Graphic Design

Requirements
Must have
• Template must be simple, elegant, classy. Please include a cover page, supporting pages (for content of presentation) and concluding ("Thank You") page. Design must include our logo & tagline (see attached), and provide recommendations for heading font, copy font and ‘bullet’ styles. Please locate company name on bottom right of template. Design should be in the same family of the look and feel of our website (www.brookvane-example.com). We would like the design to convey simplicity and elegance. We’d also like it to reflect the personality of our firm: friendly and approachable, with a high level of professionalism. Design should feel confident, and up-to-date in its look. Template must be both MAC and PC compatible.
Nice to have
• Same template developed for PPT, imported into a Prezi format as well. We need the PPT template for sure, but one in Prezi would be great to have as well - to enable more professional looking format for presentations.

```html
<!DOCTYPE html>
<html lang="en">
<head>
<meta charset="utf-8">
<title>Brookvane Presentation Template</title>
<link href="https://fonts.googleapis.com/css2?family=Crimson+Pro:wght@400;700&family=Open+Sans:wght@400;600&display=swap" rel="stylesheet">
<style>
:root{
  --orange:#f26a22;
  --blue:#1e93c8;
  --ink:#2b2b2b;
  --grey:#6d6e70;
  --bar:#58595b;
  --page:#eeeeee;
  --backdrop:#d9d9d9;
  --white:#ffffff;
}
*{margin:0;padding:0;box-sizing:border-box}
html,body{width:1200px;height:849px;overflow:hidden;background:var(--backdrop)}
.canvas{position:relative;width:1200px;height:849px}
.slide{position:absolute;width:525px;height:393px;background:linear-gradient(135deg,#f7f7f7 0%,var(--page) 55%,#dedede 100%);box-shadow:0 2px 6px rgba(0,0,0,.18);font-family:"Open Sans",Arial,sans-serif;color:var(--ink)}
.slide--cover{left:55px;top:25px;width:512px}
.slide--bullets{left:620px;top:25px}
.slide--icon{left:55px;top:433px;width:523px}
.slide--thanks{left:620px;top:433px}
.brand{position:absolute;display:flex;align-items:center;gap:6px}
.brand__mark{width:36px;height:36px;border-radius:50%;background:var(--grey);flex:none}
.brand__name{font-family:"Open Sans",Arial,sans-serif;font-weight:600;color:var(--grey);line-height:1}
.brand__tagline{font-family:"Open Sans",Arial,sans-serif;color:var(--grey);line-height:1.2}
.brand--cover{left:25px;top:15px}
.brand--cover .brand__name{font-size:28px}
.brand--cover .brand__tagline{font-size:9px}
.brand--footer{right:28px;bottom:22px;gap:4px}
.brand--footer .brand__mark{width:15px;height:15px}
.brand--footer .brand__name{font-size:13px}
.brand--footer .brand__tagline{font-size:4.5px}
.brand--large{right:28px;bottom:18px;gap:8px}
.brand--large .brand__mark{width:40px;height:40px}
.brand--large .brand__name{font-size:29px}
.brand--large .brand__tagline{font-size:9.5px}
.panel{position:absolute;background:var(--orange);border-radius:4px;color:var(--white)}
.panel--cover{left:25px;top:69px;width:471px;height:303px}
.panel--thanks{left:28px;top:16px;width:469px;height:302px}
.cover__title{position:absolute;left:28px;top:57px;font-family:"Crimson Pro",Georgia,serif;font-weight:700;font-size:25px;line-height:34px}
.cover__subtitle{position:absolute;left:28px;top:150px;font-family:"Crimson Pro",Georgia,serif;font-size:18px;line-height:25px}
.art{position:absolute;border-radius:4px}
.art--cover{left:278px;top:158px;width:180px;height:130px;background:linear-gradient(90deg,rgba(30,147,200,.45),rgba(255,255,255,.45))}
.art--network{left:258px;top:95px;width:225px;height:190px;background:radial-gradient(circle at 50% 55%,rgba(30,147,200,.3),rgba(242,106,34,.15) 45%,rgba(200,200,200,.2) 70%,transparent 78%)}
.art--handshake{left:295px;top:38px;width:150px;height:236px;background:linear-gradient(90deg,rgba(30,147,200,.45),rgba(255,255,255,.45))}
.header{position:absolute;left:28px;top:16px;width:469px;height:59px;background:var(--orange);color:var(--white);padding:8px 13px}
.slide--icon .header{left:27px}
.header__title{font-family:"Crimson Pro",Georgia,serif;font-weight:700;font-size:19px;line-height:22px}
.header__subtitle{font-family:"Crimson Pro",Georgia,serif;font-size:15px;line-height:20px}
.bullets{position:absolute;list-style:none;font-size:13px;line-height:19px}
.bullets li{position:relative;padding-left:13px}
.bullets li::before{content:"";position:absolute;left:1px;top:8px;width:4px;height:4px;border-radius:50%;background:var(--blue)}
.bullets ul{list-style:none}
.bullets--wide{left:40px;top:90px;width:430px}
.bullets--wide > li + li{margin-top:19px}
.bullets--narrow{left:40px;top:90px;width:205px}
.footer__page{position:absolute;left:40px;bottom:16px;font-family:"Crimson Pro",Georgia,serif;font-size:6.5px;color:var(--ink)}
.footer__bar{position:absolute;left:28px;right:28px;bottom:0;height:9px;background:var(--bar);border-radius:3px 3px 0 0}
.thanks__title{position:absolute;left:27px;top:120px;font-family:"Crimson Pro",Georgia,serif;font-weight:700;font-size:31px}
.social{position:absolute;left:27px;top:256px;display:flex;gap:5px}
.social__item{display:flex;align-items:center;gap:2px;font-family:"Open Sans",Arial,sans-serif;font-size:8px;color:var(--white)}
.social__item::before{content:"";width:9px;height:9px;background:rgba(255,255,255,.85);border-radius:2px}
</style>
</head>
<body>
<div class="canvas">

  <section class="slide slide--cover">
    <div class="brand brand--cover">
      <span class="brand__mark"></span>
      <div><div class="brand__name">Brookvane</div><div class="brand__tagline">Skilled people, stronger sales</div></div>
    </div>
    <div class="panel panel--cover">
      <h1 class="cover__title">Insert The Title of Your<br>Presentation Here</h1>
      <p class="cover__subtitle">Subtitle of the Presentation<br>or<br>main author’s name here</p>
      <div class="art art--cover" role="img" aria-label="Illustration of a celebrating figure and a team stacking blocks"></div>
    </div>
  </section>

  <section class="slide slide--bullets">
    <header class="header">
      <h2 class="header__title">Sample Slide - Bullet Points</h2>
      <p class="header__subtitle">Placeholder for subtitle</p>
    </header>
    <ul class="bullets bullets--wide">
      <li>The text demonstrates how your own text will look when you replace the placeholder with your own text.
        <ul>
          <li>The text demonstrates how your own text will look when you replace the placeholder with your own text.</li>
          <li>The text demonstrates how your own text will look when you replace the placeholder with your own text.</li>
        </ul>
      </li>
      <li>The text demonstrates how your own text will look when you replace the placeholder with your own text.
        <ul>
          <li>The text demonstrates how your own text will look when you replace the placeholder with your own text.</li>
          <li>The text demonstrates how your own text will look when you replace the placeholder with your own text.</li>
        </ul>
      </li>
    </ul>
    <p class="footer__page">3 &nbsp;|&nbsp; Insert the title of your presentation here</p>
    <div class="brand brand--footer">
      <span class="brand__mark"></span>
      <div><div class="brand__name">Brookvane</div><div class="brand__tagline">Skilled people, stronger sales</div></div>
    </div>
    <div class="footer__bar"></div>
  </section>

  <section class="slide slide--icon">
    <header class="header">
      <h2 class="header__title">Sample Slide - Bullet Points &amp; Icon</h2>
      <p class="header__subtitle">Placeholder for subtitle</p>
    </header>
    <ul class="bullets bullets--narrow">
      <li>The text demonstrates how your own text will look when you replace the placeholder with your own text.
        <ul>
          <li>The text demonstrates how your own text will look when you replace the placeholder with your own text.</li>
          <li>The text demonstrates how your own text will look when you replace the placeholder with your own text.</li>
        </ul>
      </li>
    </ul>
    <div class="art art--network" role="img" aria-label="Icon of a person connected to three circles of team members"></div>
    <p class="footer__page">3 &nbsp;|&nbsp; Insert the title of your presentation here</p>
    <div class="brand brand--footer">
      <span class="brand__mark"></span>
      <div><div class="brand__name">Brookvane</div><div class="brand__tagline">Skilled people, stronger sales</div></div>
    </div>
    <div class="footer__bar"></div>
  </section>

  <section class="slide slide--thanks">
    <div class="panel panel--thanks">
      <h2 class="thanks__title">Thank You</h2>
      <div class="social">
        <span class="social__item">Chirp</span>
        <span class="social__item">Faceroll</span>
        <span class="social__item">Postly</span>
        <span class="social__item">Feedr</span>
        <span class="social__item">Linkwise</span>
      </div>
      <div class="art art--handshake" role="img" aria-label="Illustration of two figures shaking hands beneath a globe of people"></div>
    </div>
    <div class="brand brand--large">
      <span class="brand__mark"></span>
      <div><div class="brand__name">Brookvane</div><div class="brand__tagline">Skilled people, stronger sales</div></div>
    </div>
  </section>

</div>
</body>
</html>
```